Honey Jar Label

I am looking for a logo for a 6oz. glass honey jar with a black lid that will contain honey from our bee boxes.
+ our product name is:  Meadow Lantern Honey
+ the label must include a Nutrition Facts label (google 'honey nutrition facts label' images for what to use).
+ dimensions:	 8 x 2.1875 inches (w x h)
+ color:	We can do one, two or three color prints. Use the VERILUX SHADE INDEX (VSI)
+ file types:  must be Adobe file (AI, PDF, PSD) or EPS files. We cannot accept other file types.
+ notes:	Gradients and halftones are strongly discouraged
+ provide all fonts with file or convert to outlines
+ design files must be CMYK, 300 dpi at 100%.

```html
<!DOCTYPE html>
<html lang="en">
<head>
<meta charset="utf-8">
<title>Meadow Lantern Honey – Jar Label</title>
<link rel="stylesheet" href="https://fonts.googleapis.com/css2?family=Dancing+Script:wght@400;500&family=Arimo:wght@400;700&display=swap">
<style>
  :root {
    --label-black: #000000;
    --label-white: #ffffff;
    --ink: #000000;
  }
  html, body {
    margin: 0;
    padding: 0;
    width: 1200px;
    height: 329px;
    overflow: hidden;
    background: var(--label-black);
  }
  .label {
    position: relative;
    width: 1200px;
    height: 329px;
    background: var(--label-black);
    overflow: hidden;
  }
  .product-name {
    position: absolute;
    left: 134px;
    top: 26px;
    width: 320px;
    margin: 0;
    font-family: "Dancing Script", cursive;
    font-weight: 400;
    font-size: 58px;
    line-height: 66px;
    color: var(--label-white);
    text-align: center;
  }
  .product-name span { display: block; }
  .product-name .underlined {
    display: inline-block;
    border-bottom: 3px solid var(--label-white);
    line-height: 62px;
    padding: 0 6px;
  }
  .panel-divider {
    position: absolute;
    left: 925px;
    top: 0;
    width: 2px;
    height: 329px;
    background: var(--label-white);
  }
  .facts-frame {
    position: absolute;
    left: 948px;
    top: 24px;
    width: 218px;
    height: 276px;
    border: 3px solid var(--label-white);
    box-sizing: border-box;
  }
  .facts {
    position: absolute;
    left: 956px;
    top: 30px;
    width: 204px;
    height: 264px;
    background: var(--label-white);
    color: var(--ink);
    font-family: Arimo, Arial, sans-serif;
  }
  .facts .row {
    position: absolute;
    left: 5px;
    right: 6px;
    font-size: 10.5px;
    line-height: 12px;
    white-space: nowrap;
  }
  .facts .row.split { display: flex; justify-content: space-between; }
  .facts .row.right { text-align: right; }
  .facts .row.indent { left: 22px; }
  .facts .title {
    position: absolute;
    left: 4px;
    top: 2px;
    font-weight: 700;
    font-size: 23px;
    line-height: 26px;
    letter-spacing: -0.3px;
  }
  .facts .serving {
    position: absolute;
    left: 5px;
    top: 30px;
    font-size: 13px;
    line-height: 15px;
  }
  .facts .rule {
    position: absolute;
    left: 4px;
    right: 4px;
    background: var(--ink);
  }
</style>
</head>
<body>
  <div class="label">
    <h1 class="product-name">
      <span>Meadow</span>
      <span>lantern</span>
      <span><span class="underlined">honey</span></span>
    </h1>

    <div class="panel-divider"></div>

    <div class="facts-frame"></div>
    <section class="facts" aria-label="Nutrition Facts">
      <div class="title">Nutrition Facts</div>
      <div class="serving">Serving Size 1 Tbsp (21 g)</div>
      <div class="rule" style="top:74px;height:5px"></div>
      <div class="row" style="top:84px">Amount Per Serving</div>
      <div class="rule" style="top:98px;height:2px"></div>
      <div class="row" style="top:102px">Calories 64</div>
      <div class="rule" style="top:115px;height:4px"></div>
      <div class="row right" style="top:121px">% Daily Value*</div>
      <div class="rule" style="top:135px;height:1px"></div>
      <div class="row split" style="top:140px"><span>Total Fat 0g</span><span>0%</span></div>
      <div class="rule" style="top:154px;height:2px"></div>
      <div class="row split" style="top:159px"><span>Sodium 0mg</span><span>0%</span></div>
      <div class="rule" style="top:173px;height:2px"></div>
      <div class="row split" style="top:179px"><span>Total Carbohydrate&nbsp; 17g</span><span>6%</span></div>
      <div class="rule" style="top:193px;height:2px"></div>
      <div class="row indent" style="top:198px">Sugars&nbsp; 16g</div>
      <div class="rule" style="top:211px;height:3px"></div>
    </section>
  </div>
</body>
</html>
```